Income Tax Business Cards - Updates

Need to update these business cards while keeping all the same wording but just update them and make them look nicer and more modern/ on brand with our brand.

Industry/Entity Type

finance

Contact Information for Business Card

we have multiple locations so will just need to easily be able to change the address and phone numbers

Colors

Designer to choose colors to be used in the design.

```html
<!DOCTYPE html>
<html lang="en">
<head>
<meta charset="utf-8">
<title>Tax Advance Business Cards</title>
<link href="https://fonts.googleapis.com/css2?family=Montserrat:wght@400;600;700;800&display=swap" rel="stylesheet">
<style>
  :root {
    --backdrop: #1f1f1f;
    --brand-green: #0f4d2c;
    --brand-red: #c21f2a;
    --paper: #ffffff;
    --ink: #1c1c1c;
    --ink-soft: #555555;
  }
  * { margin: 0; padding: 0; box-sizing: border-box; }
  html, body {
    width: 1200px; height: 988px; overflow: hidden;
    background: var(--backdrop);
    font-family: "Montserrat", sans-serif;
  }
  .canvas { position: relative; width: 1200px; height: 988px; }

  .card {
    position: absolute;
    width: 560px; height: 320px;
    border-radius: 18px;
    overflow: hidden;
  }

  /* Front card */
  .card-front {
    left: 60px; top: 130px;
    background: var(--brand-green);
    color: var(--paper);
    padding: 44px 48px;
  }
  .front-headline {
    font-weight: 800; font-size: 46px; line-height: 1;
    letter-spacing: 1px;
  }
  .front-headline .accent { color: var(--brand-red); display: block; margin-top: 4px; }
  .front-rule {
    height: 2px; background: var(--brand-red);
    margin: 22px 0 20px; width: 100%;
  }
  .front-offer { font-weight: 800; font-size: 46px; line-height: 1; letter-spacing: 1px; }
  .front-offer .amount { color: var(--brand-red); }
  .front-sub { font-weight: 800; font-size: 30px; margin-top: 10px; letter-spacing: 1px; }

  /* Back card */
  .card-back {
    left: 580px; top: 540px;
    background: var(--paper);
    color: var(--ink);
  }
  .back-band {
    position: absolute; right: 0; top: 0;
    width: 46px; height: 110px;
    background: var(--brand-red);
  }
  .back-offer {
    position: absolute; right: 66px; top: 26px;
    text-align: right;
  }
  .offer-note { font-weight: 600; font-size: 12px; letter-spacing: .5px; }
  .offer-main { font-weight: 800; font-size: 34px; line-height: 1.05; color: var(--brand-green); }
  .offer-main .amount { color: var(--brand-red); }
  .offer-sub { font-weight: 800; font-size: 21px; color: var(--brand-green); letter-spacing: .5px; }

  .brand-lockup {
    position: absolute; left: 36px; top: 160px;
    display: flex; align-items: center; gap: 10px;
  }
  .brand-dot {
    width: 14px; height: 14px; border-radius: 50%;
    background: var(--brand-red);
  }
  .brand-name { font-weight: 700; font-size: 20px; color: var(--brand-green); }

  .contact {
    position: absolute; left: 36px; bottom: 26px;
    font-style: normal;
    font-size: 15px; line-height: 1.35; color: var(--ink-soft);
  }
  .contact-phone {
    display: flex; align-items: center; gap: 8px;
    font-weight: 700; font-size: 18px; color: var(--brand-green);
    margin-top: 4px;
  }
  .contact-phone svg { width: 18px; height: 18px; }
</style>
</head>
<body>
<main class="canvas">
  <section class="card card-front">
    <h1 class="front-headline">FILE YOUR<span class="accent">TAXES HERE</span></h1>
    <div class="front-rule"></div>
    <p class="front-offer">UP TO <span class="amount">&amp;6000</span></p>
    <p class="front-sub">SAME DAY ADVANCE</p>
  </section>

  <section class="card card-back">
    <div class="back-band"></div>
    <div class="back-offer">
      <p class="offer-note">FREE ESTIMATES!</p>
      <p class="offer-main">UP TO <span class="amount">&amp;6000</span></p>
      <p class="offer-sub">SAME DAY ADVANCE</p>
      <p class="offer-note">ON APPROVED TAX RETURNS!</p>
    </div>

    <div class="brand-lockup">
      <span class="brand-dot"></span>
      <span class="brand-name">Northmark Financial Group</span>
    </div>

    <address class="contact">
      418 Maplewood Ave<br>
      Ste 3104<br>
      Lakeview AB 7240
      <span class="contact-phone">
        <svg viewBox="0 0 24 24" aria-hidden="true"><path fill="#c21f2a" d="M6.6 10.8a15.1 15.1 0 0 0 6.6 6.6l2.2-2.2a1 1 0 0 1 1-.25 11.4 11.4 0 0 0 3.6.57 1 1 0 0 1 1 1V20a1 1 0 0 1-1 1A17 17 0 0 1 3 4a1 1 0 0 1 1-1h3.5a1 1 0 0 1 1 1c0 1.25.2 2.460 .57 3.6a1 1 0 0 1-.25 1z"/></svg>
        (555) 214-7390
      </span>
    </address>
  </section>
</main>
</body>
</html>
```